Business Card Design for a Design/Build Firm

Kestrel Forge Partners, Inc. is a firm providing construction professional project management and architectural design services to an international clientele. Contemporary. "Green" movement aware. Business card to have back design/logo. Cards will be on high gloss paper

Target Market(s)

Building Developers and Owners

Industry/Entity Type

Construction

Requirements
Nice to have
• We really would like to use the acronym "KFP" as main focal point fo card design. Company will be known as KFP.
Should not have
• No globes or abstract images of buildings.

```html
<!DOCTYPE html>
<html lang="en">
<head>
<meta charset="utf-8">
<title>KFP Business Card</title>
<link rel="stylesheet" href="https://fonts.googleapis.com/css2?family=Tinos:wght@700&display=swap">
<style>
  :root {
    --stage-top: #ffffff;
    --stage-bottom-a: #ececec;
    --stage-bottom-b: #d0d0d0;
    --card-edge: #111111;
    --card-paper: #ffffff;
    --ink: #111111;
    --brand-green: #1f6a2c;
    --wash-cyan: #8fdde6;
    --wash-teal: #3f9f9a;
    --wash-green: #6bb52f;
    --wash-lime: #c9e46a;
    --band-yellow: #f3f4c8;
  }
  * { box-sizing: border-box; margin: 0; padding: 0; }
  html, body { width: 1200px; height: 1000px; overflow: hidden; }
  body {
    position: relative;
    font-family: "Tinos", "Times New Roman", serif;
    font-weight: 700;
    color: var(--ink);
    background: var(--stage-top);
  }
  .stage-lower {
    position: absolute; left: 0; top: 505px; width: 1200px; height: 495px;
    background: linear-gradient(to bottom, var(--stage-bottom-a), var(--stage-bottom-b));
  }
  .card {
    position: absolute; width: 591px; height: 339px;
    border: 2px solid var(--card-edge); border-radius: 3px;
    background: var(--card-paper); overflow: hidden;
  }
  .card--front { left: 300px; top: 96px; }
  .card--alt { left: 298px; top: 573px; }
  .card__wash {
    position: absolute; left: 60px; top: 0; right: 0; bottom: 0;
    background:
      radial-gradient(ellipse 260px 200px at 95% 100%, var(--wash-green), transparent 75%),
      radial-gradient(ellipse 200px 150px at 90% 35%, var(--wash-teal), transparent 80%),
      radial-gradient(ellipse 240px 170px at 45% 90%, var(--wash-cyan), transparent 80%),
      radial-gradient(ellipse 200px 140px at 70% 80%, var(--wash-lime), transparent 80%),
      linear-gradient(160deg, #ffffff 20%, #e6f6f3 55%, #cdeecd 100%);
  }
  .card__band { position: absolute; left: 0; top: 0; width: 591px; height: 339px; }
  .brand {
    position: absolute; color: var(--brand-green);
    font-size: 118px; line-height: 1; letter-spacing: 10px;
  }
  .card--front .brand { left: 0; width: 591px; text-align: center; top: 14px; }
  .card--alt .brand { left: 38px; top: 108px; }
  .contact {
    position: absolute; text-align: center; white-space: nowrap;
  }
  .card--front .contact { left: 0; width: 591px; top: 143px; }
  .card--alt .contact { left: 250px; width: 360px; top: 109px; }
  .contact__value { font-size: 18px; line-height: 22px; }
  .contact__label { font-size: 11px; line-height: 21px; }
  .card--alt .contact__value { line-height: 21px; }
  .card--alt .contact__label { line-height: 19px; }
</style>
</head>
<body>
  <div class="stage-lower"></div>

  <section class="card card--front">
    <div class="card__wash" role="img" aria-label="Soft abstract wash of cyan, teal and green with faint translucent squares"></div>
    <svg class="card__band" viewBox="0 0 591 339" aria-hidden="true">
      <path d="M0 68 C120 58 220 40 330 46 C430 52 520 50 591 46 L591 92 C500 96 420 80 330 86 C220 94 110 140 0 176 Z" fill="var(--band-yellow)" opacity="0.85"/>
    </svg>
    <div class="brand">KFP</div>
    <div class="contact">
      <div class="contact__value">Marcus Ellery</div>
      <div class="contact__label">Manager</div>
      <div class="contact__value">Seabrook Quarter, UAE</div>
      <div class="contact__label">Address</div>
      <div class="contact__value">02-5550198 / 0505550147</div>
      <div class="contact__label">Tel. no / Mob. no</div>
      <div class="contact__value">kestrelforgepartners.co.uk</div>
      <div class="contact__label">email add</div>
    </div>
  </section>

  <section class="card card--alt">
    <div class="card__wash" role="img" aria-label="Soft abstract wash of cyan, teal and green with faint translucent squares"></div>
    <svg class="card__band" viewBox="0 0 591 339" aria-hidden="true">
      <path d="M0 68 C120 58 220 40 330 46 C430 52 520 50 591 46 L591 92 C500 96 420 80 330 86 C220 94 110 140 0 176 Z" fill="var(--band-yellow)" opacity="0.85"/>
    </svg>
    <div class="brand">KFP</div>
    <div class="contact">
      <div class="contact__value">Marcus Ellery</div>
      <div class="contact__label">Manager</div>
      <div class="contact__value">Seabrook Quarter, UAE</div>
      <div class="contact__label">Address</div>
      <div class="contact__value">02-5550198 / 0505550147</div>
      <div class="contact__label">Tel. no / Mob. no</div>
      <div class="contact__value">kestrelforgepartners.co.uk</div>
      <div class="contact__label">email add</div>
    </div>
  </section>
</body>
</html>
```